依頼詳細
<サイトマップ>
①TOPページ
②SALON(店舗情報)
③STAFF(スタッフ紹介)
④STYLE(ギャラリー)
⑤COUPON(クーポン)
⑥FEATURE(当店の特徴)
⑦RECRUIT/COMPANY(求人・会社概要)
⑧BLOG(サイト内ブログ)
⑨NEWS(サイト内ブログ)
⑩MENU(メニュー)
⑪VOICE(お客様の声)
⑫GUEST SNAP(ゲストスナップ)

<デザインテイスト>
・ナチュラル  ・優しい  ・モダン  ・清潔な

<顧客ターゲット>
・女性
・20代~50代
①40代 ②50代 ③20代
・学生、会社員、自営業、未婚、既婚、妊婦、子育て、中年

【競合サイト】
http://www.tintlounge-mirea.j(大阪中心のカラー専門サロン)
http://www.pebble-salon.j(大きいサロン)
http://www.nuvo-ltd.co (北海道で大きいサロン)

【要望】
・pictabookのアイコンをサイト内に配置してください。
・予約が外部のためバナーなどを配置して頂けると嬉しいです。
・「VOICE」ページにはA4サイズのカウンセリングシートなどを
お客様に記入していただいたものを添付する予定ですので、TOpに
新着エリアなどがあってもうれしいです。
・ブログ、新着は新着BOXで配置して頂きたいです。

※素材は追記分内に書いています。
【素材】
■ピクセラ
素材として定期ダウンロードできる画像は使用して頂いて構いません。
その際にカンプ画像でダウンロードしてください。
(画像検索した際に出てくるサムネール下の画像番号の横にピクセラのマーク
があるものは使用不可できません・・・)
その他の素材に関しては、フリーで提供可能なものでお願いします。
■サロン外観・内装写真(ロゴ入り)
http://boxvault-example.jp/get/3f7c2d9a18e6b4c05a7d1e92f6b3c8a4d0e57f21
ダウンロードパスワード kq7vzr2t

すみません、ピクセラのURL添付し忘れてました。
https://jp.pixera-example.com/

宜しくお願いします。
今回、当サロンのコンペに閲覧・ご提案して頂きましたデザイナー様
誠にありがとうございます!!
今でもたくさんのデザイン案を提案して頂いておりますが、もう少し色々なデザイン案を見たいという事もあり、1週間コンペ期間を延長することと致しました。
依頼詳細に囚われず、色みやレイアウトもデザイナー様の自由にデザインして頂いたものをみたいので是非、提案頂ければとても嬉しいです!!
(できれば、入れて頂くページは変えないでほしいです。)
どうぞ、宜しくお願い致します。

シンプルな中にも細部までの細やかなデザインや、デザイナー様のセンスの良さもあってサロンにとてもあったデザインに仕上がっていると思います。
とても満足しています。

今回ご提案していただいたデザイナー様へ
たくさんのデザイン案を度提案頂きまして、誠にありがとうございました。
”カラー専門店”という少し珍しい業態で当サロンの良さをうまく取り入れてくださっている方が多い中で一つに絞るのが中々、大変ではありました。
どれももったいないデザインばかりでした。。。
またこのような機会がございましたら是非ご提案していただければ幸いでございます。
ありがとうございました。

```html
<!DOCTYPE html>
<html lang="ja">
<head>
<meta charset="utf-8">
<title>Tinta | ヘアカラー専門サロン ティンタ</title>
<link rel="stylesheet" href="https://fonts.googleapis.com/css2?family=Noto+Sans+JP:wght@400;500;700&family=Noto+Serif+JP:wght@400;600&family=Cormorant+Garamond:ital,wght@0,500;0,600;1,500&display=swap">
<style>
:root{
  --bg:#f3f2ef;
  --white:#ffffff;
  --ink:#555250;
  --ink-soft:#8a8784;
  --line:#dcdad5;
  --lime:#a9c23f;
  --lime-dark:#7f9a27;
  --pink:#ee8fa2;
  --sky:#e3f1f6;
  --sky-line:#bcdbe6;
  --blue:#7ea8c6;
  --beige:#efe9df;
  --gold:#e9a53a;
  --btn-gray:#9b9995;
}
*{box-sizing:border-box;margin:0;padding:0}
html,body{width:1200px;height:3232px;overflow:hidden}
body{background:var(--bg);font-family:"Noto Sans JP",sans-serif;color:var(--ink);font-size:13px;line-height:1.7}
a{color:inherit;text-decoration:none}
.wrap{width:1024px;margin:0 auto;position:relative}
.serif{font-family:"Noto Serif JP",serif}
.en{font-family:"Cormorant Garamond",serif}
.ph{display:block}

/* top bar */
.topbar{height:44px;background:var(--white);border-top:4px solid var(--lime)}
.topbar .wrap{display:flex;align-items:center;justify-content:space-between;height:40px}
.topbar .lead{font-size:11px;color:var(--ink-soft)}
.top-actions{display:flex;gap:8px;align-items:center}
.btn-reserve{background:var(--pink);color:#fff;font-size:12px;padding:4px 16px;border-radius:3px}
.btn-tel{background:var(--lime);color:#fff;font-size:13px;font-weight:700;padding:4px 14px;border-radius:3px;display:flex;gap:6px;align-items:center}
.sns-sq{width:24px;height:24px;border-radius:3px;display:inline-block}
.sns-a{background:#6cb6df}.sns-b{background:#56719f}

/* brand */
.brand{height:206px;display:flex;align-items:center;justify-content:center}
.brand-mark{display:flex;flex-direction:column;align-items:center;gap:6px}
.brand-circle{width:64px;height:64px;border-radius:50%;background:var(--lime)}
.brand-name{font-family:"Cormorant Garamond",serif;font-size:40px;font-weight:600;color:var(--ink);letter-spacing:2px}

/* nav */
.gnav{height:70px}
.gnav ul{list-style:none;display:flex;justify-content:space-between;border-bottom:1px solid var(--line);height:60px;align-items:center}
.gnav li{flex:1;text-align:center;border-left:1px solid var(--line);line-height:1.3}
.gnav li:first-child{border-left:none}
.gnav .nav-en{display:block;font-size:15px;font-weight:700;letter-spacing:1px;color:var(--ink)}
.gnav .nav-ja{display:block;font-size:10px;color:var(--lime-dark)}

/* hero */
.hero{height:420px;background:linear-gradient(90deg,#f6f2ec,#ede6da)}
.hero .wrap{height:420px}
.hero-main{position:absolute;left:0;top:0;width:520px;height:420px;background:linear-gradient(160deg,#cdbfae,#8d7766 60%,#3b2f2a)}
.hero-thumbs{position:absolute;left:600px;top:24px;display:flex;gap:14px}
.hero-thumbs .ph{width:126px;height:140px;background:linear-gradient(160deg,#e6d6c3,#9a7a62)}
.hero-copy{position:absolute;right:0;top:330px;width:420px;border-bottom:1px solid var(--ink-soft);text-align:right;padding-bottom:6px}
.hero-copy span{font-family:"Cormorant Garamond",serif;font-style:italic;font-size:40px;color:#6e6a66;letter-spacing:1px}

/* intro */
.intro{height:210px;background:var(--sky);border-bottom:1px solid var(--sky-line)}
.intro .wrap{height:210px;display:flex;justify-content:space-between;align-items:center}
.intro-text{width:640px}
.intro-text h1{font-family:"Noto Serif JP",serif;font-weight:600;font-size:22px;color:#4f6b4a;letter-spacing:2px;margin-bottom:12px}
.intro-text p{font-size:13px;color:var(--ink);line-height:1.9}
.vip-banner{width:236px;height:164px;background:#fff8e6;border:2px solid #f1d9a6;text-align:center;padding-top:14px;line-height:1.4}
.vip-banner .small{font-size:12px;color:var(--ink)}
.vip-banner .big{font-size:18px;font-weight:700;color:var(--ink)}
.vip-banner .big b{color:#e4572e;font-size:26px}
.vip-banner .pass{margin:8px auto 0;width:170px;background:#fff;border:1px solid #d9b15c;font-family:"Noto Serif JP",serif;font-size:15px;color:#8a6a2c;padding:3px 0}
.vip-banner .gift{margin:8px auto 0;width:120px;background:var(--gold);color:#fff;font-size:13px;font-weight:700;padding:3px 0}

/* panels */
.panel{background:var(--white);box-shadow:0 1px 3px rgba(0,0,0,.08)}
.features{margin-top:30px}
.features .panel{height:410px;padding:28px 28px;display:flex;gap:28px}
.feature{flex:1}
.feature .ph{height:190px;background:linear-gradient(160deg,#e8e1d8,#a79584)}
.feature:nth-child(3) .ph{background:linear-gradient(160deg,#d9d6ce,#7b8a8e)}
.feature h3{margin-top:16px;font-size:16px;font-weight:700;color:var(--lime-dark);letter-spacing:1px;border-left:4px solid var(--lime);padding-left:10px;line-height:1.3}
.feature h3 small{font-size:10px;color:var(--ink-soft);font-weight:400;margin-left:8px}
.feature p{margin-top:10px;font-size:12px;color:var(--ink);line-height:1.8}

/* coupon + galleries */
.coupon{margin-top:30px}
.coupon .panel{height:680px;padding:26px 28px}
.sec-head{display:flex;align-items:baseline;gap:10px;border-bottom:1px solid var(--line);padding-bottom:6px}
.sec-head h2{font-size:18px;font-weight:700;letter-spacing:2px;color:var(--ink)}
.sec-head span{font-size:11px;color:var(--lime-dark)}
.coupon-note{font-size:11px;color:var(--ink-soft);margin:10px 0}
.coupon-banner{height:88px;display:flex;border:1px solid var(--line)}
.coupon-banner .ph{width:420px;background:linear-gradient(90deg,#d8e6c9,#eef3e4)}
.coupon-banner .offer{flex:1;background:#fdf3f4;display:flex;align-items:center;justify-content:flex-end;gap:18px;padding-right:40px}
.offer .tag{background:var(--pink);color:#fff;font-size:11px;padding:2px 10px}
.offer .label{font-size:22px;font-weight:700;color:#7b6f6a;letter-spacing:1px}
.offer .pct{font-size:40px;font-weight:700;color:#e25a77;letter-spacing:1px}
.coupon-foot{font-size:10px;color:var(--ink-soft);margin-top:6px}
.galleries{display:flex;gap:28px;margin-top:26px}
.gallery{flex:1;border:1px solid var(--line);height:330px;position:relative;padding-top:18px}
.gallery h3{text-align:center;font-family:"Noto Serif JP",serif;font-weight:600;font-size:17px;letter-spacing:2px}
.gallery h3 small{display:block;font-family:"Noto Sans JP",sans-serif;font-size:10px;color:var(--lime-dark);font-weight:400;letter-spacing:1px}
.circles{display:flex;align-items:center;justify-content:center;gap:16px;margin-top:16px}
.circle-lg{width:150px;height:150px;border-radius:50%;background:linear-gradient(160deg,#e7d8c7,#8e735f)}
.circle-grid{display:grid;grid-template-columns:repeat(2,72px);gap:10px}
.circle-sm{width:72px;height:72px;border-radius:50%;background:linear-gradient(160deg,#eadfce,#a88b72)}
.more{position:absolute;right:16px;bottom:16px;background:var(--blue);color:#fff;font-size:10px;padding:3px 12px;letter-spacing:1px}

/* news */
.news{margin-top:40px;display:flex;gap:40px}
.news .panel{flex:1;height:470px;padding:40px 44px}
.news h2{text-align:center;font-family:"Cormorant Garamond",serif;font-size:26px;font-weight:600;letter-spacing:5px;border-bottom:1px solid var(--line);padding-bottom:14px}
.news ul{list-style:none;margin-top:10px}
.news li{border-bottom:1px dotted var(--line);padding:14px 4px;font-size:12px;line-height:1.6}
.news time{display:block;color:var(--lime-dark);font-size:11px}
.btn-list{display:block;width:180px;margin:36px auto 0;background:var(--btn-gray);color:#fff;text-align:center;font-size:12px;padding:6px 0}

/* footer */
.site-footer{margin-top:40px;background:var(--white);border-top:4px solid var(--lime);height:572px}
.site-footer .wrap{height:460px;display:flex;gap:40px;padding-top:40px}
.f-info{width:340px}
.f-brand{display:flex;align-items:center;gap:10px}
.f-brand .brand-circle{width:40px;height:40px}
.f-brand .brand-name{font-size:30px}
.f-tel{display:flex;align-items:center;gap:8px;margin-top:14px;font-size:28px;font-weight:700;color:#d9822b;letter-spacing:1px}
.f-addr{font-size:12px;margin-top:6px;line-height:1.7}
.f-map{margin-top:14px;height:170px;background:linear-gradient(135deg,#e6ebdc,#cfd9e3)}
.f-nav{flex:1;display:grid;grid-template-columns:repeat(3,1fr);align-content:start;row-gap:6px;padding-top:8px}
.f-nav a{font-size:12px;color:var(--ink)}
.f-nav a::before{content:"›";color:var(--lime-dark);margin-right:6px}
.calendar{width:230px;margin-top:8px}
.calendar caption{font-size:12px;text-align:left;padding-bottom:4px;color:var(--ink)}
.calendar table{border-collapse:collapse;width:100%}
.calendar th,.calendar td{border:1px solid var(--line);font-size:10px;text-align:center;height:24px}
.calendar th{background:#f1f0ec}
.calendar .off{background:#fbe3e8}
.f-bottom{text-align:center}
.f-bottom .sns{display:flex;justify-content:center;gap:8px;margin-bottom:12px}
.f-bottom small{font-size:10px;color:var(--ink-soft)}
</style>
</head>
<body>

<header>
  <div class="topbar">
    <div class="wrap">
      <p class="lead">湖北・みずほのヘアカラー専門サロン ティンタ 新感覚のカラー体験を</p>
      <div class="top-actions">
        <a class="btn-reserve" href="#">インターネット予約</a>
        <a class="btn-tel" href="#">
          <svg width="12" height="12" viewBox="0 0 24 24"><path fill="#fff" d="M6.6 10.8a15 15 0 0 0 6.6 6.6l2.2-2.2c.3-.3.7-.4 1-.2 1.1.4 2.3.6 3.6.6.6 0 1 .4 1 1V20c0 .6-.4 1-1 1A17 17 0 0 1 3 4c0-.6.4-1 1-1h3.5c.6 0 1 .4 1 1 0 1.3.2 2.5.6 3.6.1.3 0 .7-.2 1z"/></svg>
          077-000-1234
        </a>
        <span class="sns-sq sns-a" aria-label="chirpline"></span>
        <span class="sns-sq sns-b" aria-label="pictabook"></span>
      </div>
    </div>
  </div>
  <div class="brand">
    <div class="brand-mark">
      <span class="brand-circle"></span>
      <span class="brand-name">Tinta</span>
    </div>
  </div>
  <nav class="gnav">
    <div class="wrap">
      <ul>
        <li><a href="#"><span class="nav-en">HOME</span><span class="nav-ja">トップページ</span></a></li>
        <li><a href="#"><span class="nav-en">MENU</span><span class="nav-ja">メニュー</span></a></li>
        <li><a href="#"><span class="nav-en">SALON</span><span class="nav-ja">店舗情報</span></a></li>
        <li><a href="#"><span class="nav-en">STYLE</span><span class="nav-ja">スタイルギャラリー</span></a></li>
        <li><a href="#"><span class="nav-en">COUPON</span><span class="nav-ja">クーポン</span></a></li>
        <li><a href="#"><span class="nav-en">STAFF</span><span class="nav-ja">スタッフ紹介</span></a></li>
        <li><a href="#"><span class="nav-en">RECRUIT</span><span class="nav-ja">求人・会社概要</span></a></li>
      </ul>
    </div>
  </nav>
</header>

<main>
  <section class="hero">
    <div class="wrap">
      <div class="hero-main ph" role="img" aria-label="サロンの椅子に座る女性の写真"></div>
      <div class="hero-thumbs">
        <div class="ph" role="img" aria-label="ヘアカラースタイル写真1"></div>
        <div class="ph" role="img" aria-label="ヘアカラースタイル写真2"></div>
        <div class="ph" role="img" aria-label="ヘアカラースタイル写真3"></div>
      </div>
      <p class="hero-copy"><span>brand new myself</span></p>
    </div>
  </section>

  <section class="intro">
    <div class="wrap">
      <div class="intro-text">
        <h1>ヘアカラーを得意とした、新感覚サロン「ティンタ」</h1>
        <p>経験豊富なカラーリストが一人ひとりの髪と肌に寄り添い、<br>理想のカラーをご提案します。髪を傷めず、なりたい自分へ。<br>新しいカラーとの出会いをお楽しみください。</p>
      </div>
      <a class="vip-banner" href="#">
        <p class="small">ずっとお得をお約束!</p>
        <p class="big">先着<b>500</b>名様限定</p>
        <p class="pass">VIPパスポート</p>
        <p class="gift">プレゼント</p>
      </a>
    </div>
  </section>

  <section class="features">
    <div class="wrap">
      <div class="panel">
        <article class="feature">
          <div class="ph" role="img" aria-label="カラーリング後の女性のスタイル写真"></div>
          <h3>STYLE GALLERY<small>スタイルギャラリー</small></h3>
          <p>カラーの魅力がひと目で分かる施術例を多数掲載。季節のトレンドから定番カラーまで、あなたに似合う色がきっと見つかります。</p>
        </article>
        <article class="feature">
          <div class="ph" role="img" aria-label="笑顔のお客様の写真"></div>
          <h3>CUSTOMER'S VOICE<small>お客様の声</small></h3>
          <p>ご来店いただいたお客様から届いた感想を、カウンセリングシートとともにご紹介しています。</p>
        </article>
        <article class="feature">
          <div class="ph" role="img" aria-label="サロン入口の看板の写真"></div>
          <h3>FEATURE<small>当店の特徴</small></h3>
          <p>髪と頭皮にやさしい薬剤を厳選し、すべての施術を一貫して担当。ティンタならではのこだわりをご覧ください。</p>
        </article>
      </div>
    </div>
  </section>

  <section class="coupon">
    <div class="wrap">
      <div class="panel">
        <div class="sec-head"><h2>COUPON</h2><span>クーポン</span></div>
        <p class="coupon-note">初回ご来店の方限定のお得なクーポンです。ご予約の際にホームページを見たとお伝えください。</p>
        <a class="coupon-banner" href="#">
          <div class="ph" role="img" aria-label="新緑の背景写真"></div>
          <div class="offer">
            <span class="tag">ホームページ限定</span>
            <span class="label">ALL MENU</span>
            <span class="pct">10%OFF</span>
          </div>
        </a>
        <p class="coupon-foot">※他のクーポンとの併用はできません。有効期限はご来店日より三か月となります。</p>

        <div class="galleries">
          <div class="gallery">
            <h3>STYLING GALLERY<small>スタイリングギャラリー</small></h3>
            <div class="circles">
              <div class="circle-lg ph" role="img" aria-label="スタイリング写真メイン"></div>
              <div class="circle-grid">
                <div class="circle-sm ph" role="img" aria-label="スタイリング写真"></div>
                <div class="circle-sm ph" role="img" aria-label="スタイリング写真"></div>
                <div class="circle-sm ph" role="img" aria-label="スタイリング写真"></div>
                <div class="circle-sm ph" role="img" aria-label="スタイリング写真"></div>
              </div>
            </div>
            <a class="more" href="#">→ MORE</a>
          </div>
          <div class="gallery">
            <h3>GUEST SNAP<small>ゲストスナップ</small></h3>
            <div class="circles">
              <div class="circle-lg ph" role="img" aria-label="ゲストスナップ写真メイン"></div>
              <div class="circle-grid">
                <div class="circle-sm ph" role="img" aria-label="ゲストスナップ写真"></div>
                <div class="circle-sm ph" role="img" aria-label="ゲストスナップ写真"></div>
                <div class="circle-sm ph" role="img" aria-label="ゲストスナップ写真"></div>
                <div class="circle-sm ph" role="img" aria-label="ゲストスナップ写真"></div>
              </div>
            </div>
            <a class="more" href="#">→ MORE</a>
          </div>
        </div>
      </div>
    </div>
  </section>

  <section class="wrap news">
    <div class="panel">
      <h2>INFORMATION</h2>
      <ul>
        <li><time>2015.00.00</time>ホームページをリニューアルしました。ここに見出しが入ります。</li>
        <li><time>2015.00.00</time>夏季休業のお知らせ。ここに見出しが入ります。</li>
        <li><time>2015.00.00</time>スタッフ募集のお知らせ。ここに見出しが入ります。</li>
      </ul>
      <a class="btn-list" href="#">一覧を見る</a>
    </div>
    <div class="panel">
      <h2>BLOG</h2>
      <ul>
        <li><time>2015.00.00</time>今月のおすすめカラー。ここに見出しが入ります。</li>
        <li><time>2015.00.00</time>お家でできるヘアケア。ここに見出しが入ります。</li>
        <li><time>2015.00.00</time>スタッフの休日日記。ここに見出しが入ります。</li>
      </ul>
      <a class="btn-list" href="#">一覧を見る</a>
    </div>
  </section>
</main>

<footer class="site-footer">
  <div class="wrap">
    <div class="f-info">
      <div class="f-brand"><span class="brand-circle"></span><span class="brand-name">Tinta</span></div>
      <p class="f-tel">
        <svg width="22" height="22" viewBox="0 0 24 24"><path fill="#d9822b" d="M6.6 10.8a15 15 0 0 0 6.6 6.6l2.2-2.2c.3-.3.7-.4 1-.2 1.1.4 2.3.6 3.6.6.6 0 1 .4 1 1V20c0 .6-.4 1-1 1A17 17 0 0 1 3 4c0-.6.4-1 1-1h3.5c.6 0 1 .4 1 1 0 1.3.2 2.5.6 3.6.1.3 0 .7-.2 1z"/></svg>
        077-000-1234
      </p>
      <p class="f-addr">〒520-0000 湖北県みずほ市中央1-2-3<br>OPEN 10:00〜19:00 / 土日 9:00〜18:00<br>定休日 毎週火曜日・第三水曜日</p>
      <div class="f-map ph" role="img" aria-label="サロン周辺の地図"></div>
    </div>
    <nav class="f-nav">
      <a href="#">TOP</a><a href="#">COUPON</a><a href="#">MENU</a>
      <a href="#">SALON</a><a href="#">FEATURE</a><a href="#">VOICE</a>
      <a href="#">STAFF</a><a href="#">BLOG</a><a href="#">RECRUIT</a>
      <a href="#">STYLE GALLERY</a><a href="#">INFORMATION</a><a href="#">GUEST SNAP</a>
    </nav>
    <div class="calendar">
      <table>
        <caption>August 2015</caption>
        <tr><th>日</th><th>月</th><th>火</th><th>水</th><th>木</th><th>金</th><th>土</th></tr>
        <tr><td></td><td></td><td></td><td></td><td></td><td></td><td>1</td></tr>
        <tr><td>2</td><td>3</td><td class="off">4</td><td>5</td><td>6</td><td>7</td><td>8</td></tr>
        <tr><td>9</td><td>10</td><td class="off">11</td><td>12</td><td>13</td><td>14</td><td>15</td></tr>
        <tr><td>16</td><td>17</td><td class="off">18</td><td class="off">19</td><td>20</td><td>21</td><td>22</td></tr>
        <tr><td>23</td><td>24</td><td class="off">25</td><td>26</td><td>27</td><td>28</td><td>29</td></tr>
        <tr><td>30</td><td>31</td><td></td><td></td><td></td><td></td><td></td></tr>
      </table>
    </div>
  </div>
  <div class="f-bottom">
    <div class="sns">
      <span class="sns-sq sns-b" aria-label="pictabook"></span>
      <span class="sns-sq sns-a" aria-label="chirpline"></span>
    </div>
    <small>Copyright © Tinta. All rights reserved.</small>
  </div>
</footer>

</body>
</html>
```